Velmarone Website Redesign

We need a redesign of the company website.

We're a company, based in the UK, called Velmarone. We develop software for the Healthcare Industry, used by medical professionals throughout the UK on a daily basis.

We have a suite of tools that form the Velmarone Platform, and all are web-based.

We want to communicate that our software is not only innovative but is the best available, easy to use, and provides exceptional quality and RoI.

Additionally, we want our existing customers to be able to see what else we can offer them.

A site map is attached.
Updates

Hi Everyone,

As we approach the deadline for submissions, we’ve shortlisted threedesigns that we felt were the best of the submissions and have asked thedesigners to make some additional changes and produce some content pages so wecan see what’s beneath the Home page in the rest of the site.

Thank you all for your submissions – there was an awful lot ofdisagreement among everyone here over which designs we thought were best andsome of those that haven’t made it into the final three were very well liked.

Those in the final three have been messaged individually and have theirdesigns as the only non-eliminated ones showing. We would ask at this stagethat anyone not in the final three please do no further work or submitadditional designs as we are approaching the deadline and will not be able toprovide sufficient feedback to allow any changes in a short space of time.

Kind regards,
The Velmarone Team

Target Market(s)

Nurses and medical professionals in western-speaking countries, most notably in the UK.

Predominantly, we expect it will be senior medical staff that will be viewing (and using) our website - some will be existing customers and some will be new or potential customers.

Industry/Entity Type

Medical

Requirements
Must have
• Area to showcase and provide information about products.
• Company information - who we are and why you should choose us.
• News and events - blog, archive newsletters, publications, etc.
• Support section for existing customers - FAQ, Forum, Manuals.
• Contact page.
• We also feel that we'd like to have our telephone number and primary email address visible at all times, with an immediate ability for users to request a demonstration.
Nice to have
• A "My Velmarone" area would be nice at some point, though that's something for further down the line.

```html
<!DOCTYPE html>
<html lang="en">
<head>
<meta charset="utf-8">
<title>Velmarone Health</title>
<link href="https://fonts.googleapis.com/css2?family=Open+Sans:wght@400;600;700&family=Ubuntu:wght@400;500;700&display=swap" rel="stylesheet">
<style>
:root{
  --brand:#1e88e5;
  --panel:#29b1f6;
  --panel-head:#8ad4fa;
  --nav-top:#5ec4fa;
  --nav-bottom:#1a9ff0;
  --ink:#222;
  --muted:#444;
  --mission:#d5effd;
}
*{box-sizing:border-box;margin:0;padding:0}
html,body{width:904px;height:1200px;overflow:hidden}
body{background:#3a3a3a;font-family:"Open Sans",sans-serif}
.stage{width:1124px;height:1492px;transform:scale(.8043);transform-origin:0 0;position:relative;
  background:linear-gradient(#ffffff 0,#e4e4e4 500px,#8a8a8a 1100px,#333 1492px)}
.page{position:absolute;left:60px;top:0;width:1004px;height:1240px;background:#fdfdfd;box-shadow:0 0 14px rgba(0,0,0,.25)}
.abs{position:absolute}
.header{left:75px;top:0;width:974px;height:305px;background:linear-gradient(#9fd9f8,#d6f0fd 60%,#c6e8fb)}
.hero-photo{left:470px;top:0;width:504px;height:305px;background:radial-gradient(circle at 42% 40%,#3f6fa6 0,#9bbad6 18%,#cfe7f7 40%,rgba(200,230,250,0) 70%)}
.brand-name{left:36px;top:40px;font-family:"Ubuntu",sans-serif;font-weight:700;font-size:42px;color:var(--brand);letter-spacing:-.5px}
.intro-line{left:38px;top:104px;font-family:"Open Sans",sans-serif;font-weight:400;font-size:16px;color:#55626b}
.demo-btn{left:60px;top:159px;width:230px;height:42px;border-radius:8px;border:2px solid #6ab8e8;
  background:linear-gradient(#3b8fd8,#14509c);color:#fff;font-family:"Ubuntu",sans-serif;font-weight:700;font-size:17px;
  display:flex;align-items:center;justify-content:center}
.contact{left:76px;top:250px;font-size:14px;line-height:22px;color:var(--ink)}
.nav{left:75px;top:305px;width:974px;height:42px;display:flex}
.nav a{flex:1;display:flex;align-items:center;justify-content:center;color:#fff;font-family:Arial,sans-serif;font-size:13.5px;
  text-decoration:none;background:linear-gradient(var(--nav-top),var(--nav-bottom));border-right:1px solid #9fdcfb}
.nav a.active{background:linear-gradient(#4bb7f5,#1387e0)}
.box{left:73px;width:263px;background:var(--panel);box-shadow:-2px 2px 4px rgba(0,0,0,.15)}
.box-head{height:50px;background:linear-gradient(#b4e4fc,var(--panel-head));display:flex;align-items:center;padding-left:6px;
  font-family:Arial,sans-serif;font-size:21px;color:#111}
.box-head .dot{width:18px;height:18px;border-radius:50%;background:#9fb8c8;margin-right:8px}
.box-head .sq{width:28px;height:28px;margin-right:8px}
.box-head em{font-style:normal;color:var(--brand);margin-right:6px}
.field-label{color:#fff;font-weight:700;font-size:12.5px;letter-spacing:.4px}
.field{width:200px;height:22px;background:#fff;border:1px solid #7fb4d6}
.login-btn{display:inline-block;background:linear-gradient(#5bc3fa,#1d8ee0);color:#fff;font-size:11px;font-weight:700;padding:3px 6px;border-radius:4px;border:1px solid #b5e3fd}
.box a.link{color:#fff;font-size:11px;font-weight:700;display:block;line-height:13px}
.item{color:#fff;font-size:12.5px;line-height:14.5px;letter-spacing:.3px;position:relative;padding-left:8px}
.item::before{content:"";position:absolute;left:0;top:6px;width:5px;height:5px;border-radius:50%;background:#111}
.item b{color:#111;font-weight:700;font-size:11.5px}
.more{position:absolute;right:0;bottom:0}
.main-h{font-family:Arial,sans-serif;font-size:22px;color:#111}
.main-h em{font-style:normal;color:var(--brand)}
.copy{font-size:12.3px;line-height:14.5px;color:var(--muted);letter-spacing:.3px}
.copy strong{color:#111;font-weight:700}
.bullets{list-style:none}
.bullets li{position:relative;padding-left:12px}
.bullets li::before{content:"";position:absolute;left:0;top:5px;width:5px;height:5px;border-radius:50%;background:#111}
.photo{border:1px solid #bbb;background:linear-gradient(135deg,#e9eef2,#c9d3dc 55%,#8a96a2)}
.mission{left:349px;top:926px;width:699px;height:113px;background:var(--mission)}
.mission h3{position:absolute;left:122px;top:8px;font-family:Arial,sans-serif;font-weight:400;font-size:22px;color:var(--brand)}
.mission p{position:absolute;left:123px;top:38px;width:470px;font-size:12.3px;line-height:14.5px;color:var(--muted)}
.footer{left:48px;top:1233px;width:1027px;height:212px;background:var(--panel);font-family:"Ubuntu",sans-serif;color:#fff}
.fcol{position:absolute;top:36px;font-size:10.5px;font-weight:700;letter-spacing:.5px}
.fcol h4{font-size:11.5px;font-weight:700;padding-bottom:3px;border-bottom:1px solid #8fd3f8;margin-bottom:5px}
.fcol li{list-style:none;line-height:20px}
.copyright{position:absolute;right:16px;bottom:14px;font-size:10.5px;font-weight:700;letter-spacing:.4px}
</style>
</head>
<body>
<div class="stage">
  <div class="page"></div>

  <header class="abs header">
    <div class="abs hero-photo" role="img" aria-label="Photo of a glass globe resting on a stethoscope"></div>
    <div class="abs brand-name">Velmarone Health</div>
    <div class="abs intro-line">Web-based tools for clinical teams</div>
    <div class="abs demo-btn">Request a free Demo</div>
    <div class="abs contact">Email:support@velmarone.com<br>&nbsp;Tel: +44 (0) 20 7946 0321</div>
  </header>

  <nav class="abs nav">
    <a class="active">Home</a><a>Product &amp; services</a><a>About Velmarone</a><a>News &amp; Events</a><a>Suport</a><a>Contact Velmarone</a><a>My Velmarone</a>
  </nav>

  <section class="abs box" style="top:396px;height:234px">
    <div class="box-head"><span class="dot"></span><em>User</em>Login</div>
    <div style="padding:14px 0 0 29px">
      <div class="field-label">Username:</div>
      <div class="field" style="margin:3px 0 11px 1px"></div>
      <div class="field-label">Password:</div>
      <div class="field" style="margin:3px 0 11px"></div>
      <span class="login-btn" style="margin:0 0 10px 2px">Login</span>
      <a class="link" style="text-decoration:underline">Create new account</a>
      <a class="link" style="text-decoration:underline">Request new password</a>
    </div>
  </section>

  <section class="abs box" style="top:642px;height:231px">
    <div class="box-head"><span class="dot"></span><span class="sq" style="background:#e8e4d8"></span><em>Latest</em>News</div>
    <div style="padding:24px 24px 0 21px">
      <div class="item">In today's changing environment, healthcare organisations globally are faced with conflicting challen-ges.<b class="more">more detail</b></div>
      <div class="item" style="margin-top:14px">In today's changing environment, healthcare organisations globally are faced with conflicting challen-ges.<b class="more">more detail</b></div>
    </div>
  </section>

  <section class="abs box" style="top:886px;height:326px">
    <div class="box-head"><span class="dot"></span><span class="sq" style="background:#f26a1b;border-radius:5px"></span><em>Our</em>Blogs</div>
    <div style="padding:22px 6px 0 9px">
      <div class="item" style="padding-left:16px">In today's changing environment, healthcare organisations globally are faced with conflicting challenges.<br><b>Daniel.</b></div>
      <div class="item" style="padding-left:16px;margin-top:26px">In today's changing environment, healthcare organisations globally are faced with conflicting challenges.<br><b>Harold.</b></div>
      <div class="item" style="padding-left:16px;margin-top:26px">In today's changing environment, healthcare organisations globally are faced with conflicting challenges.<br><b>Walter.</b></div>
    </div>
  </section>

  <main>
    <h2 class="abs main-h" style="left:349px;top:394px;font-weight:400"><em>Welcome</em> To Velmarone</h2>
    <div class="abs copy" style="left:349px;top:429px;width:430px">
      <p>In today's changing environment, healthcare organisations globally are faced with conflicting challenges; to reduce costs while offering improved healthcare services to patients.</p>
      <p style="margin-top:14px">VELMARONE solutions exploit opportunities offered by the latest technological advances.</p>
      <p style="margin-top:14px"><strong>Our goal is to help:</strong></p>
      <ul class="bullets" style="margin-top:14px"><li>Reduce clinical errors</li><li>Improve patient care</li><li>Improve efficiency</li></ul>
    </div>
    <div class="abs photo" style="left:786px;top:432px;width:262px;height:188px" role="img" aria-label="Photo of a business team seated at a conference table with a laptop"></div>

    <h2 class="abs main-h" style="left:349px;top:645px;font-weight:400"><em>Velmarone</em> Solutions</h2>
    <div class="abs copy" style="left:345px;top:687px;width:435px">
      <p>Velmarone works in partnership with hospitals and healthcare professionals. Our unique approach, our partnerships with clinical specialists and our technology platform enables us to deliver highly robust and fit-for-purpose solutions.</p>
      <p style="margin-top:29px"><strong>Our Products and Services Include</strong></p>
      <ul class="bullets" style="margin-top:14px"><li style="padding-left:10px">Clinical Systems</li><li style="padding-left:10px">Clinical Audit Tools</li><li style="padding-left:10px">Technology Services</li></ul>
    </div>
    <div class="abs photo" style="left:786px;top:690px;width:262px;height:190px;background:linear-gradient(135deg,#f4f6f8,#cfe2ef 50%,#6aa6d2)" role="img" aria-label="Photo of a smiling medical team in scrubs and white coats"></div>

    <section class="abs mission">
      <svg class="abs" style="left:12px;top:0" width="86" height="52" viewBox="0 0 86 52"><g fill="#fff"><circle cx="20" cy="30" r="18"/><path d="M4 30 Q6 4 34 0 L34 8 Q16 12 14 30Z"/><circle cx="62" cy="30" r="18"/><path d="M46 30 Q48 4 76 0 L76 8 Q58 12 56 30Z"/></g></svg>
      <svg class="abs" style="left:596px;top:64px" width="96" height="49" viewBox="0 0 96 49"><g fill="#fff"><circle cx="24" cy="20" r="18"/><path d="M40 20 Q38 44 10 49 L10 41 Q28 37 30 20Z"/><circle cx="70" cy="20" r="18"/><path d="M86 20 Q84 44 56 49 L56 41 Q74 37 76 20Z"/></g></svg>
      <h3>Our Mission</h3>
      <p>Lorem Ipsum is simply dummy text of the printing and typesetting industry. Lorem Ipsum has been the industry's standard dummy text ever since the 1500s, when an unknown printer took a galley of type and scrambled it to make a type specimen book.</p>
    </section>
  </main>

  <footer class="abs footer">
    <div class="fcol" style="left:55px;width:290px"><h4>Products &amp; services</h4><ul><li>Clinical audit</li><li>Clinical systems</li><li>Software Development &amp; Intigration</li><li>Clinical concultancy</li><li>Case Studies</li><li>Demo</li></ul></div>
    <div class="fcol" style="left:400px;width:240px"><h4>About Velmarone</h4><ul><li>Leadership Team</li><li>Advisory Board</li><li>Partnerships</li><li>Experience Clinical Stall</li><li>Medical Solution Artchitects</li><li>Clients List</li></ul></div>
    <div class="fcol" style="left:659px;width:220px"><h4>News &amp; Events</h4><ul><li>Monthly News Letters</li><li>Publications</li><li>Events</li><li>Velmarone News Blogs</li></ul></div>
    <div class="fcol" style="left:906px;width:74px"><h4>Support</h4><ul><li>FAQ</li><li>Manuals</li><li>Publications</li><li>User Forums</li></ul></div>
    <div class="copyright">Copyright © 2008 Velmarone Ltd</div>
  </footer>
</div>
</body>
</html>
```